pelvo driving school postcard

I have done a very crude mock up showing the front and back of what I would like. It doesn't have to be exactly the same. I have adapted this off my website - www.pelvo.com.au. Happy to take suggestions. My clientele are mostly 16 to 20 year old, so need something to catch their attention. I need the printed product for an event I am sponsoring on the 16 November.
Target Market(s)
16 to 20 year old
Industry/Entity Type
Driving School

```html
<!DOCTYPE html>
<html lang="en">
<head>
<meta charset="utf-8">
<title>Pelvo Driving School Postcard</title>
<link href="https://fonts.googleapis.com/css2?family=Montserrat:wght@300;400;500;600;700;800&display=swap" rel="stylesheet">
<style>
  :root {
    --charcoal: #23272b;
    --charcoal-light: #2e3338;
    --brand-red: #e3161b;
    --plate-yellow: #f2c01a;
    --ink: #111111;
    --paper: #ffffff;
    --muted: #c9ccd0;
    --star: #8d9297;
    --buckle-tone: #2b2d30;
  }
  * { box-sizing: border-box; margin: 0; padding: 0; }
  html, body {
    width: 1200px; height: 1000px; overflow: hidden;
    background: var(--paper);
    font-family: "Montserrat", sans-serif;
  }
  .postcard {
    position: absolute; top: 285px; width: 572px; height: 443px;
    background: var(--paper); overflow: hidden;
    box-shadow: 0 1px 6px rgba(0,0,0,0.35);
  }
  .postcard--front { left: 17px; }
  .postcard--back { left: 606px; }

  .belt-band { position: absolute; left: 0; right: 0; background: var(--charcoal); }
  .postcard--front .belt-band { top: 37px; height: 48px; }
  .postcard--back .belt-band { top: 51px; height: 52px; left: 224px; }

  .buckle-placeholder {
    position: absolute; width: 44px; height: 68px;
    background: var(--buckle-tone);
  }
  .postcard--front .buckle-placeholder { left: 373px; top: 26px; }
  .postcard--back .buckle-placeholder { left: 185px; top: 39px; }

  .brand { position: absolute; text-align: center; }
  .brand__name {
    display: block; font-weight: 800; color: var(--brand-red);
    font-size: 38px; line-height: 1; letter-spacing: -0.5px;
  }
  .brand__tag { display: block; font-weight: 600; font-size: 12.5px; margin-top: 7px; }
  .postcard--front .brand { left: 200px; top: 17px; width: 150px; }
  .postcard--front .brand__tag { color: var(--paper); }
  .postcard--back .brand { left: 14px; top: 31px; width: 150px; }
  .postcard--back .brand__tag { color: var(--charcoal); margin-top: 10px; }

  .plate {
    position: absolute; top: 115px; width: 77px; height: 89px;
    border: 4px solid var(--ink);
    display: flex; align-items: center; justify-content: center;
    font-weight: 700; font-size: 54px;
  }
  .plate--learner { left: 72px; background: var(--plate-yellow); color: var(--ink); }
  .plate--provisional { left: 427px; background: var(--paper); color: var(--brand-red); }

  .package-headline { position: absolute; left: 150px; width: 276px; top: 129px; text-align: center; color: var(--ink); }
  .package-headline__lead { display: block; font-size: 18px; font-weight: 600; }
  .package-headline__main { display: block; font-size: 26px; font-weight: 600; margin-top: 5px; letter-spacing: -0.3px; }

  .dark-panel { position: absolute; left: 0; right: 0; }
  .postcard--front .dark-panel {
    top: 230px; bottom: 0;
    background: linear-gradient(135deg, var(--charcoal) 0%, var(--charcoal-light) 55%, var(--charcoal) 100%);
  }
  .postcard--back .dark-panel {
    top: 147px; height: 205px;
    background: linear-gradient(135deg, var(--charcoal) 0%, var(--charcoal-light) 60%, var(--charcoal) 100%);
  }

  .feature-list { position: absolute; left: 37px; top: 247px; width: 515px; list-style: none; }
  .feature-list li {
    position: relative; padding-left: 24px; margin-bottom: 13.3px;
    font-size: 10.8px; font-weight: 400; color: var(--muted);
    text-transform: uppercase; line-height: 14px;
  }
  .feature-list svg { position: absolute; left: 0; top: -1px; width: 16px; height: 16px; }

  .web-address {
    position: absolute; left: 266px; top: 64px;
    font-size: 19px; font-weight: 600; color: var(--paper); letter-spacing: 0.6px;
  }

  .booking { position: absolute; left: 52px; top: 174px; color: var(--paper); font-size: 14.5px; font-weight: 600; line-height: 19px; }
  .booking p + p { margin-top: 18px; }

  .car-photo {
    position: absolute; left: 284px; top: 168px; width: 240px; height: 155px;
    background: linear-gradient(180deg, #e9eaeb 0%, #c9cccf 100%);
  }

  .lesson-time { position: absolute; left: 52px; top: 383px; font-size: 18px; font-weight: 600; color: var(--charcoal); }
</style>
</head>
<body>

<section class="postcard postcard--front">
  <div class="belt-band"></div>
  <div class="buckle-placeholder" role="img" aria-label="Seatbelt buckle illustration"></div>
  <div class="brand">
    <span class="brand__name">Pelvo</span>
    <span class="brand__tag">Driving School</span>
  </div>

  <div class="plate plate--learner">L</div>
  <h1 class="package-headline">
    <span class="package-headline__lead">Complete Package from</span>
    <span class="package-headline__main">L Plate to P Plate</span>
  </h1>
  <div class="plate plate--provisional">P</div>

  <div class="dark-panel"></div>
  <ul class="feature-list">
    <li><svg viewBox="0 0 24 24"><path fill="var(--star)" d="M12 2l3 7 7 .6-5.3 4.7 1.6 7.2L12 17.8 5.7 21.5l1.6-7.2L2 9.6 9 9z"/></svg>Lessons available 6 days a week</li>
    <li><svg viewBox="0 0 24 24"><path fill="var(--star)" d="M12 2l3 7 7 .6-5.3 4.7 1.6 7.2L12 17.8 5.7 21.5l1.6-7.2L2 9.6 9 9z"/></svg>Free work/home/school pick's/drop off's</li>
    <li><svg viewBox="0 0 24 24"><path fill="var(--star)" d="M12 2l3 7 7 .6-5.3 4.7 1.6 7.2L12 17.8 5.7 21.5l1.6-7.2L2 9.6 9 9z"/></svg>A comprehensive range of dual controlled manual or automatic vehicles</li>
    <li><svg viewBox="0 0 24 24"><path fill="var(--star)" d="M12 2l3 7 7 .6-5.3 4.7 1.6 7.2L12 17.8 5.7 21.5l1.6-7.2L2 9.6 9 9z"/></svg>A team of experience, fully qualified, male and female instructors</li>
    <li><svg viewBox="0 0 24 24"><path fill="var(--star)" d="M12 2l3 7 7 .6-5.3 4.7 1.6 7.2L12 17.8 5.7 21.5l1.6-7.2L2 9.6 9 9z"/></svg>Senior driver assessment also available</li>
    <li><svg viewBox="0 0 24 24"><path fill="var(--star)" d="M12 2l3 7 7 .6-5.3 4.7 1.6 7.2L12 17.8 5.7 21.5l1.6-7.2L2 9.6 9 9z"/></svg>Driving lessons in a comfortable, friendly and relaxed atmosphere to ensure you get the most out of every driving lesson</li>
  </ul>
</section>

<section class="postcard postcard--back">
  <div class="belt-band"></div>
  <div class="buckle-placeholder" role="img" aria-label="Seatbelt buckle illustration"></div>
  <div class="brand">
    <span class="brand__name">Pelvo</span>
    <span class="brand__tag">Driving School</span>
  </div>
  <div class="web-address">WWW.PELVO.COM.AU</div>

  <div class="dark-panel"></div>
  <div class="booking">
    <p>TO BOOK IN A LESSON CALL<br>NEWCASTLE<br>4900 2718</p>
    <p>MAITLAND<br>4900 3141</p>
  </div>
  <div class="car-photo" role="img" aria-label="Photo of a white hatchback driving school car with roof sign"></div>

  <div class="lesson-time">LESSON TIME</div>
</section>

</body>
</html>
```